Corporate Brightfen business cards to be handed to investor, bankers etc. Needs to have a young feel

I need business cards designed for a technology company that provides uber-like rapid response on the security industry. I would like it simple but very cool and tasteful. See attached documents for artwork and colours to be used. Cut sheet describes business model. Card stock should be thicker than normal. I would like the one side to be just the art and the other to have the contact info with maybe the pin somewhere.

Target Market(s)

Investors

Industry/Entity Type

Business

Contact Information for Business Card

Would like the logo attached on one side with name address and other info on the other side.

Font styles to use
Other font styles liked:
• See existing logo

Colors
6b449b
886aae
e4daeb
ffffff

Requirements
Must have
• Name: Dorian Felkatsis
• Address: 47 Larkfield Avenue, Toronto, On, M6K2B7
• Tel: 416-7291846
• Email: rolo@brightfen.io
Nice to have
• See logo colours

```html
<!DOCTYPE html>
<html lang="en">
<head>
<meta charset="utf-8">
<title>Brightfen Business Cards</title>
<link rel="stylesheet" href="https://fonts.googleapis.com/css2?family=Roboto:wght@300;400;500&display=swap">
<style>
  :root {
    --purple: #6b449b;
    --purple-soft: #886aae;
    --lilac: #e4daeb;
    --white: #ffffff;
    --paper: #f4f2f6;
    --ink: #1d1a22;
    --stage: #ece8f0;
  }
  * { box-sizing: border-box; margin: 0; padding: 0; }
  html, body { width: 1200px; height: 800px; overflow: hidden; }
  body {
    background: var(--stage);
    font-family: "Roboto", Arial, sans-serif;
    position: relative;
  }
  .card {
    position: absolute;
    width: 490px;
    height: 280px;
    background: var(--paper);
    overflow: hidden;
    box-shadow: 0 10px 24px rgba(40, 20, 70, 0.14);
  }
  .card--front { left: 610px; top: 100px; }
  .card--back  { left: 100px; top: 420px; }

  .wordmark {
    display: flex;
    align-items: center;
    gap: 12px;
    color: var(--ink);
    font-weight: 300;
    letter-spacing: 1px;
  }
  .wordmark__dot {
    border-radius: 50%;
    background: var(--purple);
    flex: none;
  }
  .card--front .wordmark {
    position: absolute;
    left: 0; right: 0; top: 92px;
    justify-content: center;
    font-size: 54px;
  }
  .card--front .wordmark__dot { width: 22px; height: 22px; }
  .front__url {
    position: absolute;
    left: 0; right: 0; top: 190px;
    text-align: center;
    font-size: 13px;
    letter-spacing: 9px;
    color: #4a4652;
  }

  .back__disc {
    position: absolute;
    left: -10px; top: -240px;
    width: 680px; height: 680px;
    border-radius: 50%;
    background: var(--purple);
  }
  .card--back .wordmark {
    position: absolute;
    right: 28px; top: 34px;
    font-size: 44px;
  }
  .card--back .wordmark__dot {
    width: 18px; height: 18px;
    background: var(--lilac);
  }
  .contact {
    position: absolute;
    right: 28px; top: 118px;
    text-align: right;
    color: var(--white);
    font-size: 13px;
    line-height: 18px;
  }
  .contact__name {
    font-weight: 500;
    font-size: 16px;
    margin-bottom: 6px;
  }
  .contact__line {
    display: flex;
    justify-content: flex-end;
    align-items: center;
    gap: 8px;
  }
  .contact__line svg { width: 12px; height: 12px; flex: none; }
  .contact__address { margin-bottom: 4px; }
</style>
</head>
<body>

  <section class="card card--front">
    <div class="wordmark"><span class="wordmark__dot"></span>brightfen</div>
    <p class="front__url">www.brightfen.io</p>
  </section>

  <section class="card card--back">
    <div class="back__disc"></div>
    <div class="wordmark"><span class="wordmark__dot"></span>brightfen</div>
    <div class="contact">
      <p class="contact__name">Dorian Felkatsis</p>
      <p class="contact__address">47 Larkfield Avenue<br>Toronto, On, M6K2B7</p>
      <p class="contact__line">416-7291846
        <svg viewBox="0 0 24 24" aria-hidden="true"><path fill="#fff" d="M6.6 10.8a15.1 15.1 0 0 0 6.6 6.6l2.2-2.2a1 1 0 0 1 1-.25 11.4 11.4 0 0 0 3.6.57 1 1 0 0 1 1 1V20a1 1 0 0 1-1 1A17 17 0 0 1 3 4a1 1 0 0 1 1-1h3.5a1 1 0 0 1 1 1c0 1.25.2 2.45.57 3.57a1 1 0 0 1-.25 1z"/></svg>
      </p>
      <p class="contact__line">rolo@brightfen.io
        <svg viewBox="0 0 24 24" aria-hidden="true"><path fill="#fff" d="M2 5h20v14H2zm2 2v.5l8 5 8-5V7l-8 5z"/></svg>
      </p>
      <p class="contact__line">www.brightfen.io
        <svg viewBox="0 0 24 24" aria-hidden="true"><circle cx="12" cy="12" r="9" fill="none" stroke="#fff" stroke-width="2"/><path d="M3 12h18M12 3c3 3 3 15 0 18M12 3c-3 3-3 15 0 18" fill="none" stroke="#fff" stroke-width="1.6"/></svg>
      </p>
    </div>
  </section>

</body>
</html>
```